Brivora Collective Business Card Design

We need a business card design for Brivora Collective. We are a healthcare recruiting, wellness and education company. We partner with medical facilities to find quality candidates. We also offer free wellness courses.
The final design should communicate an emphasis on recruiting and wellness
The main purpose of the business card is to utilized it for networking events, give to hospitals, executives, VCs surgery centers and clinics. I want it to be sleek, clean, use of our brand colors and professional.

```html
<!DOCTYPE html>
<html lang="en">
<head>
<meta charset="utf-8">
<title>Brivora Collective – Business Card</title>
<link href="https://fonts.googleapis.com/css2?family=Fraunces:opsz,wght@9..144,400&family=Montserrat:wght@500&display=swap" rel="stylesheet">
<style>
  :root {
    --stage: #cbcbcb;
    --teal-deep: #005b55;
    --teal-bright: #00857a;
    --lime-soft: #e3ef8f;
    --paper: #ffffff;
    --label: #f4f4f4;
    --serif: "Fraunces", Georgia, serif;
    --sans: "Montserrat", Arial, sans-serif;
  }
  * { box-sizing: border-box; margin: 0; padding: 0; }
  html, body { width: 1200px; height: 1104px; overflow: hidden; }
  body { background: var(--stage); position: relative; font-family: var(--serif); }
  h2, h3 { font-weight: 400; }

  .card {
    position: absolute; left: 268px; width: 682px; height: 408px;
    box-shadow: 8px 14px 22px rgba(0,0,0,0.28);
    overflow: hidden;
  }
  .card-front { top: 62px; background: var(--teal-deep); }
  .card-back { top: 536px; background: var(--paper); }

  /* front */
  .portrait-area {
    position: absolute; left: 0; top: 0; width: 189px; height: 284px;
    background: linear-gradient(180deg, #00786f 0%, #006c64 100%);
    border-bottom-right-radius: 30px;
  }
  .front-brand {
    position: absolute; left: 106px; top: 282px; width: 262px; height: 82px;
    display: flex; align-items: center; justify-content: flex-end; gap: 14px; color: var(--paper);
  }
  .brand-square { width: 22px; height: 22px; background: currentColor; border-radius: 4px; flex: none; }
  .brand-name { font-family: var(--serif); font-weight: 400; line-height: 1.02; text-align: right; flex: none; }
  .front-brand .brand-name { font-size: 34px; }
  .front-divider {
    position: absolute; left: 380px; top: 270px; width: 2px; height: 99px; background: var(--paper);
  }
  .tagline {
    position: absolute; left: 390px; top: 274px; width: 285px;
    color: var(--paper); font-size: 24px; line-height: 30px; letter-spacing: -0.2px; white-space: nowrap;
  }

  /* back */
  .top-band { position: absolute; left: 33px; top: 0; width: 616px; height: 12px; background: var(--teal-deep); }
  .back-brand {
    position: absolute; left: 33px; top: 26px; width: 168px; height: 168px;
    display: flex; flex-direction: column; align-items: center; justify-content: center; gap: 14px;
    color: var(--teal-deep);
  }
  .back-brand .brand-square { width: 40px; height: 40px; border-radius: 6px; }
  .back-brand .brand-name { font-size: 33px; text-align: center; }
  .section-tag {
    position: absolute; left: 222px; width: 151px; height: 26px;
    background: var(--teal-deep); color: var(--paper); border-radius: 2px;
    font-size: 19px; line-height: 26px; text-align: center;
  }
  .tag-mission { top: 26px; }
  .tag-solutions { top: 168px; }
  .mission-text {
    position: absolute; left: 222px; top: 59px; width: 427px;
    color: var(--teal-deep); font-size: 18px; line-height: 24.8px; letter-spacing: -0.3px; text-align: justify;
  }
  .audience {
    position: absolute; top: 208px; width: 304px; height: 33px;
    border: 1.5px solid var(--teal-deep); border-radius: 4px;
    color: var(--teal-deep); font-size: 16px; line-height: 30px; text-align: center; white-space: nowrap;
  }
  .audience-left { left: 33px; }
  .audience-right { left: 346px; }
  .benefits {
    position: absolute; top: 254px; width: 303px; height: 84px;
    background: var(--lime-soft); border-radius: 6px;
    list-style: none; padding-top: 4px;
    color: var(--teal-deep); font-size: 14.6px; line-height: 25.3px; letter-spacing: -0.2px; white-space: nowrap;
    overflow: hidden;
  }
  .benefits-left { left: 33px; padding-left: 10px; }
  .benefits-right { left: 346px; padding-left: 22px; }
  .benefits li::before { content: "+"; font-weight: 700; margin-right: 5px; }
  .bottom-band {
    position: absolute; left: 33px; top: 352px; width: 616px; height: 56px;
    background: var(--teal-deep); color: var(--paper);
    font-family: var(--sans); font-weight: 500; font-size: 26px; letter-spacing: 2.4px;
    line-height: 56px; text-align: center; white-space: nowrap;
  }

  /* dimension marks */
  .dimension { position: absolute; }
  .dim-label { position: absolute; color: var(--label); font-family: Arial, Helvetica, sans-serif; font-size: 28px; white-space: nowrap; }
  .dim-height-label { left: 72px; top: 722px; }
  .dim-width-label { left: 541px; top: 1018px; }
</style>
</head>
<body>

<section class="card card-front" aria-label="Card front">
  <div class="portrait-area" role="img" aria-label="Teal tinted illustration of a healthcare professional in a white coat with a stethoscope, writing on a tablet"></div>
  <div class="front-brand">
    <span class="brand-square"></span>
    <span class="brand-name">Brivora<br>Collective</span>
  </div>
  <div class="front-divider"></div>
  <p class="tagline">Transforming the<br>healthcare<br>employment experience</p>
</section>

<section class="card card-back" aria-label="Card back">
  <div class="top-band"></div>
  <div class="back-brand">
    <span class="brand-square"></span>
    <span class="brand-name">Brivora<br>Collective</span>
  </div>
  <h2 class="section-tag tag-mission">Our Mission</h2>
  <p class="mission-text">We provide wellness and career support to healthcare professionals, connection with local medical centers, and sustainable employment solutions.</p>
  <h2 class="section-tag tag-solutions">Our Solutions</h2>
  <h3 class="audience audience-left">For Hospitals &amp; Medical Practices</h3>
  <h3 class="audience audience-right">For Medical Professionals</h3>
  <ul class="benefits benefits-left">
    <li>Recruit Quality Healthcare Workers</li>
    <li>Streamlined Hiring Process</li>
    <li>Consistently Retain Quality Employees</li>
  </ul>
  <ul class="benefits benefits-right">
    <li>Accessible Wellness Benefits</li>
    <li>Supportive Healthcare Community</li>
    <li>Career Trajectory Support</li>
  </ul>
  <div class="bottom-band">www.brivoracollective.com</div>
</section>

<svg class="dimension" style="left:228px;top:556px" width="30" height="370" aria-hidden="true">
  <polyline points="27,2 2,2 2,366 27,366" fill="none" stroke="var(--label)" stroke-width="2"/>
</svg>
<span class="dim-label dim-height-label">2 inches</span>

<svg class="dimension" style="left:288px;top:958px" width="644" height="34" aria-hidden="true">
  <polyline points="2,2 2,31 641,31 641,2" fill="none" stroke="var(--label)" stroke-width="2"/>
</svg>
<span class="dim-label dim-width-label">3.5 inches</span>

</body>
</html>
```